Design concept Visual UI of future mobile app - healthcare

Hi,
I'm looking for a top designer, innovative with strong experience in user interface

The app will be connected to a future health website related to depression and addiction by helping the user to track the moods, tired, anxiety using this mobile app.

I attached the deck of the overall project but I can send you a specific presentation for the app only

thanks

Target Market(s)

Switzerland, UK, Germany and France

Industry/Entity Type

Mental Health

Logo Text

Health, hope

Font styles to use
Sans Serif

Colors
cee9f5
33a6d7
0692cd
0255a3
3276b5
85abd2

Requirements
Must have
• keep it simple, easy to navigate
• The user should be able to track the moods on a daily basis,
• sleep time, and rate how the feel on the day
• To be able to get information from the care ledger of vornel
Nice to have
• to be able share this app with a friend

```html
<!DOCTYPE html>
<html lang="en">
<head>
<meta charset="utf-8">
<title>Health, hope – app screens</title>
<link href="https://fonts.googleapis.com/css2?family=Roboto:wght@400;500;700&display=swap" rel="stylesheet">
<style>
  :root {
    --canvas: #f2f2f2;
    --sky-top: #2f95d6;
    --sky-mid: #4aa7e0;
    --sky-low: #6bb9e8;
    --bar: rgba(255,255,255,0.10);
    --white: #ffffff;
    --ink: #6f6f6f;
    --rule: #8a8a8a;
    --button: #2c5a82;
    --menu-bg: rgba(40,120,190,0.55);
  }
  * { margin: 0; padding: 0; box-sizing: border-box; }
  html, body { width: 1200px; height: 800px; overflow: hidden; background: var(--canvas); }
  body { position: relative; font-family: "Roboto", Arial, sans-serif; color: var(--white); }

  .screen { position: absolute; top: 227px; width: 189px; height: 335px; overflow: hidden; }
  .screen--profile { left: 233px; }
  .screen--setting { left: 510px; }
  .screen--menu { left: 786px; }
  .sky { position: absolute; inset: 0;
    background: radial-gradient(ellipse at 50% 35%, rgba(255,255,255,0.18), transparent 60%),
                linear-gradient(180deg, var(--sky-top) 0%, var(--sky-mid) 55%, var(--sky-low) 100%); }

  .status { position: absolute; top: 3px; left: 4px; right: 4px; height: 10px; font-size: 5.5px; display: flex; justify-content: space-between; align-items: center; }
  .status__time { position: absolute; left: 50%; transform: translateX(-50%); }
  .battery { display: inline-block; width: 11px; height: 5px; background: var(--white); border-radius: 1px; margin-left: 2px; vertical-align: middle; }

  .topbar { position: absolute; top: 22px; left: 0; right: 0; height: 20px; background: var(--bar); }
  .topbar__menu { position: absolute; left: 20px; top: 6px; }
  .topbar__back { position: absolute; left: 38px; top: 5px; }
  .topbar__next { position: absolute; right: 20px; top: 5px; }
  .topbar__title { position: absolute; left: 0; right: 0; top: 5px; text-align: center; font-size: 8px; font-weight: 700; letter-spacing: .2px; }
  .topbar__title svg { vertical-align: -1px; margin-right: 2px; }

  .label { position: absolute; left: 35px; font-size: 5.5px; font-weight: 700; }
  .field { position: absolute; background: var(--white); border-radius: 5px; }
  .unit { position: absolute; font-size: 5px; opacity: .9; }
  .radio { position: absolute; top: 94px; font-size: 5.5px; }
  .radio::before { content: ""; display: inline-block; width: 4px; height: 4px; border-radius: 50%; background: var(--white); margin-right: 4px; vertical-align: 0; }

  .card { position: absolute; left: 31px; width: 125px; background: var(--white); }
  .card__row { position: relative; height: 19px; line-height: 19px; padding-left: 6px; font-size: 6px; color: var(--ink); }
  .card__row + .card__row { border-top: 1px solid #bdbdbd; }
  .card__row--tall { height: 22px; line-height: 22px; }
  .card__row svg { position: absolute; right: 5px; top: 6px; }
  .invite .card__row { height: 23px; line-height: 23px; border-top: none; }
  .invite .card__row::after { content: ""; position: absolute; left: 6px; right: 4px; bottom: 0; height: 1px; background: var(--rule); }
  .invite__button { position: absolute; left: 30px; top: 271px; width: 126px; height: 22px; background: var(--button); font-size: 7.5px; text-align: center; line-height: 22px; }

  .menu { position: absolute; left: 8px; top: 45px; width: 110px; height: 125px; background: var(--menu-bg); }
  .menu__item { position: absolute; left: 6px; font-size: 5.5px; font-weight: 700; white-space: nowrap; }
  .menu__item svg { vertical-align: -1px; margin-right: 1px; }
  .menu__sub { position: absolute; left: 20px; font-size: 5.5px; white-space: nowrap; }
  .menu__chev { position: absolute; }
  .menu__logout { position: absolute; left: 88px; top: 109px; }
</style>
</head>
<body>

<!-- Profile screen -->
<section class="screen screen--profile">
  <div class="sky" role="img" aria-label="Soft blue sky with light clouds"></div>
  <div class="status"><span>●●●○○ NORA</span><span class="status__time">4:21 PM</span><span>100%<i class="battery"></i></span></div>
  <header class="topbar">
    <svg class="topbar__menu" width="10" height="8" viewBox="0 0 10 8"><path d="M0 1h10M0 4h10M0 7h10" stroke="#fff" stroke-width="1.2"/></svg>
    <svg class="topbar__back" width="6" height="10" viewBox="0 0 6 10"><path d="M5 1L1 5l4 4" fill="none" stroke="#fff" stroke-width="1"/></svg>
    <div class="topbar__title"><svg width="7" height="8" viewBox="0 0 7 8"><circle cx="3.5" cy="2" r="2" fill="#fff"/><path d="M0 8c0-3 1.5-4 3.5-4S7 5 7 8z" fill="#fff"/></svg>PROFILE</div>
    <svg class="topbar__next" width="6" height="10" viewBox="0 0 6 10"><path d="M1 1l4 4-4 4" fill="none" stroke="#fff" stroke-width="1"/></svg>
  </header>

  <span class="label" style="top:49px">Name</span>
  <div class="field" style="left:35px;top:61px;width:114px;height:10px"></div>
  <span class="label" style="top:80px">Gender</span>
  <span class="radio" style="left:66px">Male</span>
  <span class="radio" style="left:102px">Female</span>
  <span class="label" style="top:104px">Age</span>
  <div class="field" style="left:35px;top:115px;width:32px;height:10px"></div>
  <span class="label" style="top:133px">Height</span>
  <div class="field" style="left:35px;top:145px;width:21px;height:10px"></div>
  <span class="unit" style="left:58px;top:148px">ft</span>
  <div class="field" style="left:68px;top:145px;width:21px;height:10px"></div>
  <span class="unit" style="left:92px;top:148px">in</span>
  <span class="label" style="top:164px">Weight</span>
  <div class="field" style="left:35px;top:176px;width:22px;height:10px"></div>
  <span class="unit" style="left:59px;top:179px">lbs</span>
  <span class="label" style="top:193px">Medications</span>
  <div class="field" style="left:35px;top:205px;width:115px;height:26px"></div>
  <span class="label" style="top:241px">Consultations</span>
  <div class="field" style="left:35px;top:253px;width:115px;height:27px"></div>
</section>

<!-- Setting screen -->
<section class="screen screen--setting">
  <div class="sky" role="img" aria-label="Soft blue sky with light clouds"></div>
  <div class="status"><span>●●●○○ NORA</span><span class="status__time">4:21 PM</span><span>100%<i class="battery"></i></span></div>
  <header class="topbar">
    <svg class="topbar__menu" width="10" height="8" viewBox="0 0 10 8"><path d="M0 1h10M0 4h10M0 7h10" stroke="#fff" stroke-width="1.2"/></svg>
    <svg class="topbar__back" width="6" height="10" viewBox="0 0 6 10"><path d="M5 1L1 5l4 4" fill="none" stroke="#fff" stroke-width="1"/></svg>
    <div class="topbar__title"><svg width="8" height="8" viewBox="0 0 8 8"><circle cx="4" cy="4" r="2.6" fill="none" stroke="#fff" stroke-width="1.6" stroke-dasharray="1.2 0.6"/><circle cx="4" cy="4" r="1" fill="#fff"/></svg>SETTING</div>
    <svg class="topbar__next" width="6" height="10" viewBox="0 0 6 10"><path d="M1 1l4 4-4 4" fill="none" stroke="#fff" stroke-width="1"/></svg>
  </header>

  <div class="card" style="top:53px">
    <div class="card__row">Version 1.0.0<svg width="5" height="8" viewBox="0 0 5 8"><path d="M1 0.5l3 3.5-3 3.5" fill="none" stroke="#777" stroke-width=".8"/></svg></div>
    <div class="card__row">More info<svg width="5" height="8" viewBox="0 0 5 8"><path d="M1 0.5l3 3.5-3 3.5" fill="none" stroke="#777" stroke-width=".8"/></svg></div>
  </div>
  <div class="card" style="top:112px">
    <div class="card__row card__row--tall">Follow us on Pagebook<svg width="5" height="8" viewBox="0 0 5 8"><path d="M1 0.5l3 3.5-3 3.5" fill="none" stroke="#777" stroke-width=".8"/></svg></div>
    <div class="card__row card__row--tall">Follow us on Chirper<svg width="5" height="8" viewBox="0 0 5 8"><path d="M1 0.5l3 3.5-3 3.5" fill="none" stroke="#777" stroke-width=".8"/></svg></div>
    <div class="card__row card__row--tall">Care Ledger - App<svg width="5" height="8" viewBox="0 0 5 8"><path d="M1 0.5l3 3.5-3 3.5" fill="none" stroke="#777" stroke-width=".8"/></svg></div>
  </div>
  <div class="card invite" style="top:202px">
    <div class="card__row">Your name</div>
    <div class="card__row">Friend name</div>
    <div class="card__row">Friend email</div>
  </div>
  <div class="invite__button">Invite your friend</div>
</section>

<!-- Menu screen -->
<section class="screen screen--menu">
  <div class="sky" role="img" aria-label="Soft blue sky with light clouds"></div>
  <div class="status"><span>●●●○○ NORA</span><span class="status__time">4:21 PM</span><span>100%<i class="battery"></i></span></div>
  <header class="topbar">
    <svg class="topbar__menu" width="10" height="8" viewBox="0 0 10 8"><path d="M0 1h10M0 4h10M0 7h10" stroke="#fff" stroke-width="1.2"/></svg>
    <svg class="topbar__back" width="6" height="10" viewBox="0 0 6 10"><path d="M5 1L1 5l4 4" fill="none" stroke="#fff" stroke-width="1"/></svg>
    <div class="topbar__title">SETTING</div>
    <svg class="topbar__next" width="6" height="10" viewBox="0 0 6 10"><path d="M1 1l4 4-4 4" fill="none" stroke="#fff" stroke-width="1"/></svg>
  </header>

  <nav class="menu">
    <span class="menu__item" style="top:6px"><svg width="7" height="6" viewBox="0 0 7 6"><path d="M3.5 0L0 3h1v3h2V4h1v2h2V3h1z" fill="#fff"/></svg>HOME SCREEN</span>
    <svg class="menu__chev" style="left:66px;top:6px" width="5" height="8" viewBox="0 0 5 8"><path d="M1 .5l3 3.5-3 3.5" fill="none" stroke="#fff" stroke-width=".8"/></svg>
    <span class="menu__sub" style="top:19px">HOW I FEEL TODAY</span>
    <svg class="menu__chev" style="left:100px;top:19px" width="5" height="8" viewBox="0 0 5 8"><path d="M1 .5l3 3.5-3 3.5" fill="none" stroke="#fff" stroke-width=".8"/></svg>
    <span class="menu__sub" style="top:32px">TRACKING GRAPHS</span>
    <svg class="menu__chev" style="left:100px;top:32px" width="5" height="8" viewBox="0 0 5 8"><path d="M1 .5l3 3.5-3 3.5" fill="none" stroke="#fff" stroke-width=".8"/></svg>
    <span class="menu__sub" style="top:45px">PERSONAL INFORMATION</span>
    <svg class="menu__chev" style="left:100px;top:45px" width="5" height="8" viewBox="0 0 5 8"><path d="M1 .5l3 3.5-3 3.5" fill="none" stroke="#fff" stroke-width=".8"/></svg>

    <span class="menu__item" style="top:58px"><svg width="8" height="6" viewBox="0 0 8 6"><rect x=".5" y=".5" width="6" height="5" fill="none" stroke="#fff" stroke-width=".8"/><path d="M2 3l1.5 1.5L7.5 0" fill="none" stroke="#fff" stroke-width=".8"/></svg>ACTIVITY</span>
    <svg class="menu__chev" style="left:54px;top:58px" width="5" height="8" viewBox="0 0 5 8"><path d="M1 .5l3 3.5-3 3.5" fill="none" stroke="#fff" stroke-width=".8"/></svg>
    <span class="menu__item" style="top:71px"><svg width="7" height="6" viewBox="0 0 7 6"><rect x=".5" y=".5" width="6" height="5" fill="#fff"/><path d="M.5 .5l3 2.5 3-2.5" fill="none" stroke="#3a8fd0" stroke-width=".7"/></svg>MESSAGES</span>
    <svg class="menu__chev" style="left:54px;top:71px" width="5" height="8" viewBox="0 0 5 8"><path d="M1 .5l3 3.5-3 3.5" fill="none" stroke="#fff" stroke-width=".8"/></svg>
    <span class="menu__item" style="top:84px"><svg width="6" height="7" viewBox="0 0 7 8"><circle cx="3.5" cy="2" r="2" fill="#fff"/><path d="M0 8c0-3 1.5-4 3.5-4S7 5 7 8z" fill="#fff"/></svg>PROFILE</span>
    <svg class="menu__chev" style="left:54px;top:84px" width="5" height="8" viewBox="0 0 5 8"><path d="M1 .5l3 3.5-3 3.5" fill="none" stroke="#fff" stroke-width=".8"/></svg>
    <span class="menu__item" style="top:97px"><svg width="7" height="7" viewBox="0 0 8 8"><circle cx="4" cy="4" r="2.6" fill="none" stroke="#fff" stroke-width="1.6" stroke-dasharray="1.2 0.6"/><circle cx="4" cy="4" r="1" fill="#fff"/></svg>SETTING</span>
    <svg class="menu__chev" style="left:54px;top:97px" width="5" height="8" viewBox="0 0 5 8"><path d="M1 .5l3 3.5-3 3.5" fill="none" stroke="#fff" stroke-width=".8"/></svg>

    <svg class="menu__logout" width="12" height="11" viewBox="0 0 12 11"><rect x="8" y="0" width="3" height="11" fill="#fff"/><path d="M0 5.5h6M4 3l2.5 2.5L4 8" fill="none" stroke="#fff" stroke-width="1.4"/></svg>
  </nav>
</section>

</body>
</html>
```